The Lantern Protocol: A Practical Guide for Tending Old Orchards

This will be for both the hard cover and paperback version. A core theme of the book and what we want to cover to convey is the journey or transformation to "happiness". Concepts such as road/pathway, mountain top, sunrise, dark to bright colors, out-of-focus to in-focus, clouds parting, etc., all represent this idea. I am attaching a 1-page book summary for more information. I like the idea of the subtitle being in a gold seal, but that is not necessary. I am open to any designs, but it should at least be conceptually related to the book.

```html
<!DOCTYPE html>
<html lang="en">
<head>
<meta charset="utf-8">
<title>The Lantern Protocol — Book Cover</title>
<link rel="stylesheet" href="https://fonts.googleapis.com/css2?family=Bebas+Neue&family=Lora:wght@400;700&family=Poppins:wght@500&display=swap">
<style>
  :root {
    --sky-top: #b8522a;
    --sky-mid: #d9733a;
    --horizon: #e89a55;
    --ridge: #6a3420;
    --ground: #2a1510;
    --ground-deep: #140a08;
    --sun: #fff6d8;
    --text: #ffffff;
  }
  * { margin: 0; padding: 0; box-sizing: border-box; }
  html, body {
    width: 801px;
    height: 1200px;
    overflow: hidden;
    background: var(--ground-deep);
  }
  .cover {
    position: relative;
    width: 801px;
    height: 1200px;
    overflow: hidden;
    color: var(--text);
    text-align: center;
  }
  .cover-art {
    position: absolute;
    inset: 0;
    background:
      radial-gradient(circle at 160px 230px, var(--sun) 0, rgba(255,240,200,0.85) 30px, rgba(255,200,120,0.35) 80px, rgba(255,180,100,0) 180px),
      linear-gradient(180deg, var(--sky-top) 0%, var(--sky-mid) 25%, var(--horizon) 42%, var(--ridge) 58%, var(--ground) 78%, var(--ground-deep) 100%);
  }
  .series-line {
    position: absolute;
    top: 58px;
    left: 0;
    right: 0;
    font-family: "Lora", serif;
    font-weight: 400;
    font-size: 28px;
    letter-spacing: 0.2px;
  }
  .subtitle-lead {
    position: absolute;
    top: 247px;
    left: 0;
    right: 0;
    font-family: "Poppins", sans-serif;
    font-weight: 500;
    font-size: 34px;
    letter-spacing: -0.5px;
    text-shadow: 0 1px 6px rgba(0,0,0,0.25);
  }
  .subtitle-main {
    position: absolute;
    top: 296px;
    left: 0;
    right: 0;
    font-family: "Bebas Neue", sans-serif;
    font-weight: 400;
    font-size: 150px;
    line-height: 140px;
    letter-spacing: 1px;
    text-shadow: 0 2px 10px rgba(0,0,0,0.25);
  }
  .subtitle-main span { display: block; }
  .author {
    position: absolute;
    top: 1068px;
    left: 0;
    right: 0;
    font-family: "Lora", serif;
    font-weight: 700;
    font-size: 64px;
    letter-spacing: 0.5px;
  }
</style>
</head>
<body>
  <main class="cover">
    <div class="cover-art" role="img" aria-label="Illustration of a stone path winding through grassy hills toward mountains under a glowing orange sunrise sky"></div>
    <p class="series-line">The Lantern Protocol:</p>
    <h1>
      <span class="subtitle-lead">A Practical Guide for</span>
      <span class="subtitle-main"><span>Tending</span><span>Old Orchards</span></span>
    </h1>
    <p class="author">Martin E. Holloway</p>
  </main>
</body>
</html>
```